New business stationairy

I need paper with header and footer and business cards.
I am a Ltd Company and my main field of expertise is QA/QC inspection in the Oil and Gas Industry. I will need all contact detail inserted and a footer with registration number and bank details etc

Industry/Entity Type

Business

```html
<!DOCTYPE html>
<html lang="en">
<head>
<meta charset="utf-8">
<title>Halden Inspection Services Ltd – Letterhead Options</title>
<link rel="stylesheet" href="https://fonts.googleapis.com/css2?family=PT+Sans+Narrow:wght@400;700&family=Arimo:wght@400&display=swap">
<style>
  :root {
    --navy: #26347f;
    --red: #b8222a;
    --paper: #ffffff;
    --watermark: #e6e7ef;
    --label: #eeeeee;
    --bg-light: #8c8c8c;
    --bg-dark: #3c3c3c;
    --ink: #2a3478;
  }
  * { box-sizing: border-box; margin: 0; padding: 0; }
  html, body { width: 1200px; height: 1000px; overflow: hidden; }
  body {
    position: relative;
    background: linear-gradient(135deg, var(--bg-light) 0%, #666 45%, var(--bg-dark) 100%);
    font-family: "PT Sans Narrow", "Arial Narrow", sans-serif;
  }

  .sheet {
    position: absolute;
    background: var(--paper);
    overflow: hidden;
  }
  .sheet--1 { left: 26px;  top: 12px;  width: 371px; height: 480px; }
  .sheet--2 { left: 418px; top: 12px;  width: 371px; height: 480px; }
  .sheet--3 { left: 811px; top: 12px;  width: 371px; height: 480px; }
  .sheet--4 { left: 190px; top: 525px; width: 359px; height: 465px; }
  .sheet--5 { left: 562px; top: 525px; width: 358px; height: 467px; }

  .option-label {
    position: absolute;
    font-family: "Arimo", Arial, sans-serif;
    font-size: 17px;
    color: var(--label);
  }

  /* Brand block */
  .brand {
    position: absolute;
    top: 24px;
    display: flex;
    align-items: center;
    gap: 5px;
  }
  .brand--left { left: 27px; }
  .brand--center { left: 50%; transform: translateX(-50%); }
  .brand__dot {
    width: 12px; height: 12px;
    border-radius: 50%;
    background: var(--red);
  }
  .brand__name {
    font-weight: 700;
    font-size: 11px;
    color: var(--navy);
    white-space: nowrap;
  }

  /* Faint background name */
  .watermark {
    position: absolute;
    font-weight: 700;
    font-size: 92px;
    line-height: 1;
    color: var(--watermark);
    white-space: nowrap;
  }

  /* Contact block */
  .contact {
    position: absolute;
    display: flex;
    align-items: stretch;
    gap: 4px;
    font-family: "Arimo", Arial, sans-serif;
    font-size: 5px;
    line-height: 1.45;
    color: var(--ink);
  }
  .contact__address { text-align: right; padding-right: 4px; border-right: 0.6px solid var(--navy); padding-top: 1px; }
  .contact__lines { display: flex; flex-direction: column; gap: 2px; }
  .contact__item { display: flex; align-items: center; gap: 3px; white-space: nowrap; }
  .contact__icon {
    width: 6px; height: 6px;
    background: var(--navy);
    border-radius: 1px;
    display: block;
  }
  .contact--light { color: #fff; }
  .contact--light .contact__address { border-right-color: #fff; }
  .contact--light .contact__icon { background: #fff; }

  .footer-art { position: absolute; left: 0; bottom: 0; display: block; }
</style>
</head>
<body>

  <!-- Option 1 -->
  <section class="sheet sheet--1" aria-label="Letterhead option 1">
    <div class="brand brand--left"><span class="brand__dot"></span><span class="brand__name">Halden Inspection Services Ltd</span></div>
    <div class="watermark" style="left:200px; top:316px;">Halden</div>
    <div class="contact" style="left:24px; top:448px;">
      <div class="contact__address">The Willows, Mill Road, Ashby,<br>Marlow Vale, Devon, EX12 4RT</div>
      <div class="contact__lines">
        <span class="contact__item"><span class="contact__icon"></span>07700 900418</span>
        <span class="contact__item"><span class="contact__icon"></span>office@haldenqa.co.uk</span>
      </div>
    </div>
    <svg class="footer-art" width="371" height="14" viewBox="0 0 371 14">
      <path d="M0 2 H234 C244 2 248 6 252 14 H0 Z" fill="var(--navy)"/>
      <path d="M246 2 H371 V14 H260 C257 7 253 3 246 2 Z" fill="var(--red)"/>
    </svg>
  </section>
  <span class="option-label" style="left:51px; top:499px;">Letterhead 1</span>

  <!-- Option 2 -->
  <section class="sheet sheet--2" aria-label="Letterhead option 2">
    <div class="brand brand--left"><span class="brand__dot"></span><span class="brand__name">Halden Inspection Services Ltd</span></div>
    <div class="contact" style="right:30px; top:38px;">
      <div class="contact__address">The Willows, Mill Road, Ashby,<br>Marlow Vale, Devon, EX12 4RT</div>
      <div class="contact__lines">
        <span class="contact__item"><span class="contact__icon"></span>07700 900418</span>
        <span class="contact__item"><span class="contact__icon"></span>office@haldenqa.co.uk</span>
      </div>
    </div>
    <div class="watermark" style="left:56px; top:214px;">Halden</div>
    <svg class="footer-art" width="371" height="14" viewBox="0 0 371 14">
      <path d="M0 2 H234 C244 2 248 6 252 14 H0 Z" fill="var(--navy)"/>
      <path d="M246 2 H371 V14 H260 C257 7 253 3 246 2 Z" fill="var(--red)"/>
    </svg>
  </section>
  <span class="option-label" style="left:677px; top:499px;">Letterhead 2</span>

  <!-- Option 3 -->
  <section class="sheet sheet--3" aria-label="Letterhead option 3">
    <div class="brand brand--left"><span class="brand__dot"></span><span class="brand__name">Halden Inspection Services Ltd</span></div>
    <div class="contact" style="right:30px; top:38px;">
      <div class="contact__address">The Willows, Mill Road, Ashby,<br>Marlow Vale, Devon, EX12 4RT</div>
      <div class="contact__lines">
        <span class="contact__item"><span class="contact__icon"></span>07700 900418</span>
        <span class="contact__item"><span class="contact__icon"></span>office@haldenqa.co.uk</span>
      </div>
    </div>
    <div class="watermark" style="left:196px; top:318px;">Halden</div>
    <svg class="footer-art" width="371" height="40" viewBox="0 0 371 40" preserveAspectRatio="none">
      <path d="M0 6 C120 -2 220 8 300 19 C330 23 355 21 371 16 V20 C350 26 320 27 290 23 C210 13 120 2 0 10 Z" fill="var(--red)"/>
      <path d="M0 13 C120 5 220 16 290 26 C330 31 355 25 371 12 V40 H0 Z" fill="var(--navy)"/>
    </svg>
  </section>
  <span class="option-label" style="left:1071px; top:499px;">Letterhead 3</span>

  <!-- Option 4 -->
  <section class="sheet sheet--4" aria-label="Letterhead option 4">
    <div class="brand brand--left"><span class="brand__dot"></span><span class="brand__name">Halden Inspection Services Ltd</span></div>
    <div class="watermark" style="left:-14px; top:306px;">Halden</div>
    <div class="contact" style="left:184px; top:436px;">
      <div class="contact__address">The Willows, Mill Road, Ashby,<br>Marlow Vale, Devon, EX12 4RT</div>
      <div class="contact__lines">
        <span class="contact__item"><span class="contact__icon"></span>07700 900418</span>
        <span class="contact__item"><span class="contact__icon"></span>office@haldenqa.co.uk</span>
      </div>
    </div>
    <svg class="footer-art" width="359" height="8" viewBox="0 0 359 8">
      <rect x="0" y="0" width="359" height="8" fill="var(--navy)"/>
    </svg>
  </section>
  <span class="option-label" style="left:49px; top:962px;">Letterhead 4</span>

  <!-- Option 5 -->
  <section class="sheet sheet--5" aria-label="Letterhead option 5">
    <div class="brand brand--center"><span class="brand__dot"></span><span class="brand__name">Halden Inspection Services Ltd</span></div>
    <div class="watermark" style="left:178px; top:300px;">Halden</div>
    <svg class="footer-art" width="358" height="42" viewBox="0 0 358 42" preserveAspectRatio="none">
      <path d="M0 4 C120 -2 215 6 290 14 C320 17 345 14 358 8 V12 C340 20 315 22 285 19 C205 11 115 3 0 9 Z" fill="var(--red)"/>
      <path d="M0 12 C115 6 210 14 280 22 C315 26 342 20 358 9 V42 H0 Z" fill="var(--navy)"/>
    </svg>
    <div class="contact contact--light" style="left:30px; top:444px;">
      <div class="contact__address">The Willows, Mill Road, Ashby,<br>Marlow Vale, Devon, EX12 4RT</div>
      <div class="contact__lines">
        <span class="contact__item"><span class="contact__icon"></span>07700 900418</span>
        <span class="contact__item"><span class="contact__icon"></span>office@haldenqa.co.uk</span>
      </div>
    </div>
  </section>
  <span class="option-label" style="left:959px; top:962px;">Letterhead 5</span>

</body>
</html>
```